Business Card for Orvane Parts Wholesale supplier

Hi There! I need a new business card for our company. We are specialized in selling Orvane parts, mostly we sell new LCD screens for Telvox and Slatrons. I would like to see that back in the design.

You can find the colors and logo's on our website: www.dorvak-example.nl

Industry/Entity Type

Business

Contact Information for Business Card

My Details:
Lars Vintorp

Phone: 0031612873406
E-mail: Lars@dorvak-example.nl

Slogan: "Because Quality Matters"

Font styles to use
Sans Serif

Colors

Designer to choose colors to be used in the design.

Requirements
Must have
• A Black backside with the Dorvak logo on it. The front side should be clean with only my contact details.
• But I'm also open for something really different or awesome!
Nice to have
• Remember that we are in the parts & repairing industry, So i'll be handing those business cards mainly to repair companies. Maybe you can do something with that thought :)

```html
<!DOCTYPE html>
<html lang="en">
<head>
<meta charset="utf-8">
<title>Dorvak Business Card</title>
<link href="https://fonts.googleapis.com/css2?family=Montserrat:wght@500;600;700;800&display=swap" rel="stylesheet">
<style>
  :root {
    --stage-top: #1c1b21;
    --stage-bottom: #3a3842;
    --card-white: #ffffff;
    --card-black: #050505;
    --ink: #111111;
    --orange: #e5913d;
    --logo-white: #ffffff;
  }
  * { margin: 0; padding: 0; box-sizing: border-box; }
  html, body {
    width: 1200px; height: 1173px; overflow: hidden;
  }
  body {
    background: linear-gradient(180deg, var(--stage-top), var(--stage-bottom));
    font-family: "Montserrat", sans-serif;
    position: relative;
  }
  .card {
    position: absolute;
    left: 180px;
    width: 840px;
    height: 480px;
    border-radius: 30px;
    overflow: hidden;
    box-shadow: 0 24px 50px rgba(0,0,0,0.45);
  }
  .card-front { top: 70px; background: var(--card-white); }
  .card-back { top: 620px; background: var(--card-black); }

  .brand {
    display: flex; align-items: center; gap: 22px;
  }
  .brand-dot {
    width: 78px; height: 78px; border-radius: 50%;
    background: var(--orange);
    flex: none;
  }
  .brand-name {
    font-weight: 800; font-size: 96px; letter-spacing: 1px; line-height: 1;
    white-space: nowrap;
  }
  .card-front .brand { position: absolute; left: 60px; top: 92px; gap: 16px; }
  .card-front .brand-dot { width: 58px; height: 58px; }
  .card-front .brand-name { color: var(--ink); font-size: 66px; }

  .holder-name {
    position: absolute; left: 62px; top: 200px;
    font-size: 30px; font-weight: 600; color: var(--ink);
    white-space: nowrap;
  }

  .contact-list {
    position: absolute; right: 50px; top: 78px;
    list-style: none;
    display: flex; flex-direction: column; gap: 22px; align-items: flex-end;
  }
  .contact-item {
    display: flex; align-items: center; gap: 12px;
    font-size: 19px; font-weight: 600; color: var(--ink);
    white-space: nowrap;
  }
  .contact-icon { width: 34px; height: 34px; flex: none; }

  .slogan-band {
    position: absolute; left: 0; right: 0; bottom: 0; height: 112px;
    background: var(--orange);
    display: flex; align-items: center; justify-content: center;
  }
  .slogan {
    color: var(--card-white); font-size: 50px; font-weight: 600; letter-spacing: 0.5px;
    white-space: nowrap;
  }

  .card-back .brand {
    position: absolute; left: 50%; top: 50%; transform: translate(-50%, -50%);
  }
  .card-back .brand-name { color: var(--logo-white); }
</style>
</head>
<body>

<section class="card card-front" aria-label="Business card front">
  <div class="brand">
    <span class="brand-dot"></span>
    <span class="brand-name">dorvak</span>
  </div>
  <p class="holder-name">Lars Vintorp</p>

  <ul class="contact-list">
    <li class="contact-item">
      <span>0031612873406</span>
      <svg class="contact-icon" viewBox="0 0 36 36" aria-hidden="true">
        <circle cx="18" cy="18" r="18" fill="#e5913d"/>
        <path d="M12 10c1-1 2.5-1 3 0l1.5 3c.4.8 0 1.6-.6 2l-1 .8c.8 2 2.3 3.5 4.3 4.3l.8-1c.4-.6 1.2-1 2-.6l3 1.5c1 .5 1 2 0 3l-1.4 1.4c-1 1-3 1.2-5.5-.2-3-1.7-5.5-4.2-7.2-7.2-1.4-2.5-1.2-4.5-.2-5.5z" fill="#fff"/>
      </svg>
    </li>
    <li class="contact-item">
      <span>Lars@dorvak-example.nl</span>
      <svg class="contact-icon" viewBox="0 0 36 36" aria-hidden="true">
        <circle cx="18" cy="18" r="18" fill="#e5913d"/>
        <rect x="9" y="12" width="18" height="12" rx="1" fill="none" stroke="#fff" stroke-width="2"/>
        <path d="M9.5 12.5L18 19l8.5-6.5" fill="none" stroke="#fff" stroke-width="2"/>
      </svg>
    </li>
    <li class="contact-item">
      <span>www.dorvak-example.nl</span>
      <svg class="contact-icon" viewBox="0 0 36 36" aria-hidden="true">
        <circle cx="18" cy="18" r="18" fill="#e5913d"/>
        <circle cx="18" cy="18" r="9" fill="none" stroke="#fff" stroke-width="2"/>
        <ellipse cx="18" cy="18" rx="4" ry="9" fill="none" stroke="#fff" stroke-width="1.6"/>
        <path d="M9 18h18" stroke="#fff" stroke-width="1.6"/>
      </svg>
    </li>
  </ul>

  <div class="slogan-band">
    <p class="slogan">Because Quality Matters</p>
  </div>
</section>

<section class="card card-back" aria-label="Business card back">
  <div class="brand">
    <span class="brand-dot"></span>
    <span class="brand-name">dorvak</span>
  </div>
</section>

</body>
</html>
```